Business Card design for an International Import Export House

We need a Business Card design for our import export business. We trade in Minerals, Metals, Rice, Sugar, Steel etc.. The design should be minimalistic. It may or may not contain the physical address. In case you want to include the physical address - 418 Verandah Heights, Marlow Sector 9, Kestrel Bay, Ardena, India, 560417.

Target Market(s)

Steel Mills or Steel Plants, Factories, Mining businesses, Industrial houses, Government Agencies

Industry/Entity Type

Importer

Contact Information for Business Card

Business Name - Tessan Overseas

Font styles to use
Other font styles liked:
• montserrat

Requirements
Must have
• Ravi Kandola - President
• www.tessanoverseas.com
• ravi@tessanoverseas.com
• +91-987-654-3217
Nice to have
• Trusted traders of metals

```html
<!DOCTYPE html>
<html lang="en">
<head>
<meta charset="utf-8">
<title>Tessan Overseas – Business Card</title>
<link rel="stylesheet" href="https://fonts.googleapis.com/css2?family=Montserrat:wght@600;700&family=Open+Sans:wght@400;600;700&display=swap">
<style>
  :root {
    --backdrop: #1c1d1f;
    --paper: #ffffff;
    --panel: #1d2023;
    --teal: #4aa3b8;
    --divider: #4a4e52;
    --text-light: #f2f4f5;
    --text-muted: #c9ced2;
  }
  * { box-sizing: border-box; margin: 0; padding: 0; }
  html, body {
    width: 1200px; height: 873px; overflow: hidden;
    background: var(--backdrop);
  }
  .canvas {
    width: 1200px; height: 873px;
    display: flex; align-items: center; justify-content: center; gap: 44px;
  }
  .card {
    width: 540px; height: 309px;
    background: var(--paper);
    position: relative; overflow: hidden;
    box-shadow: 0 12px 30px rgba(0,0,0,.45);
  }

  /* Front */
  .card-front { display: flex; }
  .brand-panel {
    width: 44%; position: relative;
    display: flex; align-items: center; justify-content: center;
  }
  .brand-panel::before {
    content: ""; position: absolute; top: 0; left: 0; right: 0; height: 9px;
    background: var(--teal); border-bottom-right-radius: 14px;
  }
  .brand { display: flex; align-items: center; gap: 10px; }
  .brand-dot { width: 18px; height: 18px; border-radius: 50%; background: var(--teal); flex: none; }
  .brand-name {
    font-family: "Montserrat", sans-serif; font-weight: 700;
    color: var(--teal); font-size: 19px; line-height: 1.15;
    text-transform: uppercase; letter-spacing: .5px;
  }
  .contact-panel {
    width: 56%; background: var(--panel); color: var(--text-light);
    padding: 24px 22px 0 26px;
    font-family: "Open Sans", sans-serif;
  }
  .person-name { font-weight: 700; font-size: 24px; line-height: 1.1; }
  .person-role { font-weight: 600; font-size: 13px; color: var(--text-muted); margin: 3px 0 11px; }
  .contact-list { list-style: none; }
  .contact-item {
    display: flex; align-items: center; gap: 11px;
    border-top: 1px solid var(--divider);
    padding: 8px 0; font-size: 12.5px; line-height: 1.4;
    white-space: nowrap;
  }
  .contact-item svg { flex: none; width: 18px; height: 18px; }

  /* Back */
  .card-back { display: flex; flex-direction: column; }
  .back-brand { flex: 1; display: flex; align-items: center; justify-content: center; }
  .back-brand .brand-name { font-size: 26px; }
  .back-brand .brand-dot { width: 24px; height: 24px; }
  .tagline-band {
    height: 36px; background: var(--teal);
    display: flex; align-items: center; justify-content: center;
    font-family: "Open Sans", sans-serif; font-weight: 600;
    color: var(--paper); font-size: 12.5px; letter-spacing: 4px; text-transform: uppercase;
  }
</style>
</head>
<body>
<main class="canvas">

  <section class="card card-front" aria-label="Business card front">
    <div class="brand-panel">
      <div class="brand">
        <span class="brand-dot"></span>
        <span class="brand-name">Tessan<br>Overseas</span>
      </div>
    </div>
    <div class="contact-panel">
      <h1 class="person-name">Ravi Kandola</h1>
      <p class="person-role">President</p>
      <ul class="contact-list">
        <li class="contact-item">
          <svg viewBox="0 0 20 20" fill="none" stroke="#4aa3b8" stroke-width="1.5"><circle cx="10" cy="10" r="9"/><rect x="7" y="5" width="6" height="10" rx="1"/></svg>
          +91-987-654-3217
        </li>
        <li class="contact-item">
          <svg viewBox="0 0 20 20" fill="none" stroke="#4aa3b8" stroke-width="1.5"><circle cx="10" cy="10" r="9"/><rect x="5.5" y="7" width="9" height="6.5"/><path d="M5.5 7l4.5 3.5L14.5 7"/></svg>
          ravi@tessanoverseas.com
        </li>
        <li class="contact-item">
          <svg viewBox="0 0 20 20" fill="none" stroke="#4aa3b8" stroke-width="1.5"><circle cx="10" cy="10" r="9"/><circle cx="10" cy="10" r="5"/><path d="M5 10h10M10 5c2 2.5 2 7.5 0 10M10 5c-2 2.5-2 7.5 0 10"/></svg>
          www.tessanoverseas.com
        </li>
        <li class="contact-item">
          <svg viewBox="0 0 20 20" fill="none" stroke="#4aa3b8" stroke-width="1.5"><circle cx="10" cy="10" r="9"/><path d="M10 15s-3.5-3.6-3.5-6a3.5 3.5 0 0 1 7 0c0 2.4-3.5 6-3.5 6z"/><circle cx="10" cy="9" r="1.1"/></svg>
          <span>418 Verandah Heights,<br>Marlow Sector 9, Kestrel Bay,<br>Ardena, India, 560417.</span>
        </li>
      </ul>
    </div>
  </section>

  <section class="card card-back" aria-label="Business card back">
    <div class="back-brand">
      <div class="brand">
        <span class="brand-dot"></span>
        <span class="brand-name">Tessan<br>Overseas</span>
      </div>
    </div>
    <div class="tagline-band">Trusted traders of metals</div>
  </section>

</main>
</body>
</html>
```